Tarn - Stationary Design/Layout

We are a well established clothing design and manufacturing company (Tarn Sourcing) based in London UK, with our own factory in Bangladesh, supplying to many fashion retailers and brands. Our factory has very high environmental and ethical standards with people at its heart. Our quality of garments are second to none.
Our new logo has been proudly developed by the Pixel Guild community last month, we are now in the second phase and need the layout designed for our letterheads, double sided business cards, compliment slip and clothing ticket. Feel as creative as you like, but make sure it looks great!!
***The Logo - the logo design and colour is set and should NOT be changed and stay on a dark grey backround. The logo artwork to use is attached.
***Details to use for the business card:
Dorian Pelham
Direct Line: 020 7946 0158
dorian@tarnsourcing-example.com
Tarn Sourching Ltd.
57 - 59 Hollin Row
Camdon . Swindon
NW9 4QT
Switchboard: 020 7946 0274
Fax: 020 7946 0274
www.tarnsourcing-example.co.uk
***Details to use for the letterhead and compliment slip:
Tarn Sourching Ltd.
57 - 59 Hollin Row
Camdon . Swindon
NW9 4QT
Fax: 020 7946 0274
www.tarnsourcing-example.co.uk
***Details for Swing Ticket:
Size: 12cm height by 5.5cm width
One side need to have just the logo without the 'Sourcing', on the other it needs to stay blank

```html
<!DOCTYPE html>
<html lang="en">
<head>
<meta charset="utf-8">
<title>Tarn Sourcing – Stationery</title>
<link rel="stylesheet" href="https://fonts.googleapis.com/css2?family=Barlow:wght@400;600&family=Arimo&display=swap">
<style>
:root{
  --ink:#3f3b39;
  --mist:#bfe2e6;
  --mark:#c2e8ec;
  --text:#4a4644;
  --soft:#8a8886;
  --rule:#b9b9b9;
  --paper:#ffffff;
}
*{margin:0;padding:0;box-sizing:border-box}
html,body{width:1200px;height:955px;overflow:hidden;background:var(--paper)}
body{position:relative;font-family:"Barlow",sans-serif;color:var(--text)}
.caption{position:absolute;font-size:7.5px;letter-spacing:.4px;color:var(--text)}

/* wordmark */
.wordmark{position:absolute;color:var(--mark);font-family:"Barlow",sans-serif;font-weight:400;line-height:1;text-align:right}
.wordmark .name{display:block;letter-spacing:3px}
.wordmark .line{display:block;letter-spacing:.6px}

/* letterhead */
.letterhead{position:absolute;left:75px;top:73px;width:577px;height:815px;border:1px solid var(--rule);background:var(--paper)}
.lh-top{position:absolute;left:0;top:0;width:100%;height:71px;background:var(--mist)}
.lh-band{position:absolute;left:0;top:71px;width:100%;height:60px;background:var(--ink)}
.lh-address{position:absolute;left:69px;top:15px;font-size:9px;line-height:10.6px;color:var(--text);letter-spacing:.3px}
.lh-address b{font-weight:600}
.lh-contact{position:absolute;left:201px;top:15px;font-size:9px;line-height:10.6px;color:var(--text);letter-spacing:.3px}
.key{color:#fff;font-weight:600;margin-right:6px}
.letter{position:absolute;left:69px;font-family:"Arimo",sans-serif;font-size:9.6px;line-height:11.7px;color:#333}
.fold{position:absolute;left:-1px;width:8px;height:1px;background:var(--rule)}
.lh-foot{position:absolute;left:69px;top:803px;font-size:7px;line-height:8.8px;color:var(--soft);letter-spacing:.3px}

/* cards */
.card{position:absolute;width:230px;height:150px}
.dark{background:var(--ink)}
.light{background:var(--mist)}
.c-text{position:absolute;font-size:6.8px;line-height:8.8px;letter-spacing:.15px;color:#cfe6e8;white-space:nowrap}
.c-name{font-size:10.5px;letter-spacing:.6px;color:#e6f2f3;margin-bottom:4px}
.c-text b{font-weight:600;color:#fff}
.c-text .k{display:inline-block;min-width:12px;font-weight:600;color:#fff}
.on-light{color:var(--text)}
.on-light .c-name{color:#fff}
.on-light b{color:var(--text)}
.on-light .k{color:#fff}

/* swing ticket */
.ticket-back{position:absolute;left:790px;top:578px;width:155px;height:335px;background:var(--mist);transform:rotate(-6deg);transform-origin:top left;box-shadow:2px 3px 6px rgba(0,0,0,.2)}
.ticket{position:absolute;left:765px;top:584px;width:151px;height:329px;background:var(--ink);box-shadow:2px 3px 6px rgba(0,0,0,.3)}
.hole{position:absolute;left:70px;top:20px;width:11px;height:11px;border-radius:50%;background:#fff}
.ticket .wordmark{left:-44px;top:168px;width:240px;transform:rotate(-90deg);text-align:left}
</style>
</head>
<body>

<!-- Letterhead -->
<section class="letterhead">
  <div class="lh-top">
    <p class="lh-address"><b>Tarn Sourching Limited</b><br>57-59 Hollin Row<br>Camdon<br>London NW9 4QT</p>
    <p class="lh-contact"><span class="key">T</span>020 7946 0274<br><span class="key">F</span>020 7946 0274<br><span class="key">W</span>tarnsourcing-example.com</p>
  </div>
  <div class="lh-band">
    <div class="wordmark" style="right:40px;top:10px">
      <span class="name" style="font-size:30px">TARN</span>
      <span class="line" style="font-size:9px;margin-top:2px">SOURCING</span>
    </div>
  </div>
  <span class="fold" style="top:157px"></span>
  <span class="fold" style="top:297px"></span>
  <span class="fold" style="top:421px"></span>

  <p class="letter" style="top:155px">Mr B Hale<br>14 Larchfield Road<br>Kelmscott<br>Londo W7 2ZQ</p>
  <p class="letter" style="top:155px;left:208px">16 May 2011</p>
  <p class="letter" style="top:280px">Dear Mr and Mrs B Hale</p>
  <div class="letter" style="top:304px;width:470px">
    <p>Peros doleniat accum del dolortionum nibh exerilisit dolore volorperos et, sequam ex ero odignisim zzriustin veliscilla facin eniam, venim ate conse dolobor at veliquatue volobortin volor sed ent aliquam, consecte facilit lore te vulla commodio dolor in vullutatue modionsequi te molorpe raesecte te volorperat lore magnim irillum il ut luptatum num ip ese eu facin ulla con henim dolore eummy nulla core feuipsumsan velisl in hent la feuis do do odolore doluptat. Cum vullaore et, quat at luptat irilis aut ipis aliquatem vel ese tatum do dolor sit utpat irilisim quisl in ute magna consequatio diamet prat. Ut utat delesto dio dolenim doluptat. Duisl ullaorem iniam irit auguerostrud min henim zzrit nisi.</p>
    <p style="margin-top:11.7px">Em amcommo dolenibh er ip eliquis nonse velit dunt ipit utem qui ex etuerating et ut accumsa ndionsecte endio conulla feugiat. Ut digna commolorper susto odipit accumsa ndigna faccumsan velestisis numsandipis do etuerci ncincilis nos et, quam venit nullaortinim er ipsum del ut wis ad te duissenit, sum velit autpatu eraesto consequam, sequis nulla alit ulputpat adionsed ea alit ipsusto do doluptate consecte magnim zzriusc iduisi.</p>
    <p style="margin-top:11.7px">La aute ex eril eugait ex et aliqui tie mod eugiamet at lutatissecte ea feugue tatetue conum dolore magniatie faccumsan hendion senibh enit lumsan hent lum illum eum dolenim volendigna feui ting euis augait, susto consecte consequate magnisim in velis ea feum ad elenim ing enis nis nulput nullutatum zzriliquat. Agnisciduis eui tie modit praese modolor sim nullupt atinim ipit ipit utet wisim irit pratio dipsustrud eugiamet dunt iurerci tie faccum qui eliquam conulputatet am do conum aut laore eumsan utpatem diat. Ut niam quis nim vendre commy nos auguerillam iliquisl iliquis niscinciduis acidunt autate facincil ulla autpat praestio od ex et, quat aut prat. Loborem iure faccum vendit aciduisim am iusto duis adio od tem eum dolor iliscidunt adiat.</p>
  </div>
  <p class="letter" style="top:593px">Kind Regards</p>
  <p class="letter" style="top:663px">Dorian Pelham</p>
  <p class="lh-foot">VAT 000 0000 00<br>Registered in England no. 0000000</p>
</section>

<!-- Option 1 -->
<div class="card dark" style="left:670px;top:107px">
  <div class="wordmark" style="right:50px;top:60px">
    <span class="name" style="font-size:30px">TARN</span>
    <span class="line" style="font-size:9px;margin-top:2px">SOURCING</span>
  </div>
</div>
<div class="card light" style="left:910px;top:107px">
  <div class="c-text on-light" style="left:106px;top:26px;font-size:6.5px;letter-spacing:0">
    <p class="c-name">Dorian Pelham</p>
    <p><span class="k">DL</span>020 7946 0158<br><span class="k">E</span>dorian@tarnsourcing-example.com</p>
    <p style="margin-top:14px"><b>Tarn Sourching Limited</b><br>57-59 Hollin Row<br>Camdon<br>London NW9 4QT<br><span class="k">T</span>020 7946 0274<br><span class="k">F</span>020 7946 0274<br><span class="k">W</span>tarnsourcing-example.com</p>
  </div>
</div>
<p class="caption" style="left:670px;top:265px">Option 1 - Front &amp; back</p>

<!-- Option 2 -->
<div class="card light" style="left:689px;top:348px;height:157px"></div>
<div class="card dark" style="left:670px;top:329px;height:149px">
  <div class="wordmark" style="right:13px;top:21px">
    <span class="name" style="font-size:27px">TARN</span>
    <span class="line" style="font-size:8px;margin-top:2px">SOURCING</span>
  </div>
  <div class="c-text" style="left:10px;top:82px;font-size:6.2px;letter-spacing:0">
    <p class="c-name">Dorian Pelham</p>
    <p><span class="k" style="min-width:10px">DL</span>020 7946 0158<br><span class="k" style="min-width:10px">E</span>dorian@tarnsourcing-example.com</p>
  </div>
  <div class="c-text" style="left:140px;top:80px;font-size:6.2px;line-height:7.8px;letter-spacing:0">
    <p><b style="color:var(--mark)">Tarn Sourching Limited</b><br>57-59 Hollin Row<br>Camdon<br>London NW9 4QT<br><span class="k" style="min-width:10px">T</span>020 7946 0274<br><span class="k" style="min-width:10px">F</span>020 7946 0274<br><span class="k" style="min-width:10px">W</span>tarnsourcing-example.com</p>
  </div>
</div>
<p class="caption" style="left:670px;top:509px">Option 2 - Front &amp; back</p>

<!-- Option 3 -->
<div class="card light" style="left:989px;top:329px;width:151px;height:229px"></div>
<div class="card dark" style="left:971px;top:310px;width:151px;height:229px">
  <div class="wordmark" style="right:10px;top:26px">
    <span class="name" style="font-size:30px">TARN</span>
    <span class="line" style="font-size:9px;margin-top:2px">SOURCING</span>
  </div>
  <div class="c-text" style="left:11px;top:110px;font-size:6.5px;letter-spacing:0">
    <p class="c-name">Dorian Pelham</p>
    <p><span class="k">DL</span>020 7946 0158<br><span class="k">E</span>dorian@tarnsourcing-example.com</p>
    <p style="margin-top:14px"><b style="color:var(--mark)">Tarn Sourching Limited</b><br>57-59 Hollin Row<br>Camdon<br>London NW9 4QT<br><span class="k">T</span>020 7946 0274<br><span class="k">F</span>020 7946 0274<br><span class="k">W</span>tarnsourcing-example.com</p>
  </div>
</div>
<p class="caption" style="left:969px;top:571px">Option 3 - Front &amp; back</p>

<!-- Swing ticket -->
<div class="ticket-back"></div>
<div class="ticket">
  <span class="hole"></span>
  <div class="wordmark">
    <span class="name" style="font-size:46px;letter-spacing:6px">TARN</span>
    <span class="line" style="font-size:12px;margin-top:3px;padding-left:122px">SOURCING</span>
  </div>
</div>
<p class="caption" style="left:969px;top:830px">Swing ticket - Front &amp; back</p>

</body>
</html>
```